Need simple and modern looking business card with all my information on one side and logo on the other side
Info :
Company name - VELMAR CONSTRUCTION LLC
Company addres- 418 harbor 87th. Dunmoor park ny 10352
Email- velmarllc@tridomail.Com
Company phone number 555-318-6094
Cell number- 555-742-0583
Web site - velmarllc.Com
My name Gerald tomasino

Target Market(s)

Construction , home improvement, remodeling

Industry/Entity Type

Construction

Contact Information for Business Card

It has to be moder but at the same time simple

Font styles to use
Sans Serif

Colors
0255a3
ffffff
000000
f78f20
b1b1b1
9d9d9d
1b1b1b
33a6d7
ec1f27

Requirements
Must have
• My logo on one side maybe with a some kind of background on the other side all my information
Nice to have
• Some kind of background pictures provided by you .PLEASE HAVE ACCOUNT WITH PIXELVAULT WILL NOT PAY ANY EXTRA FEES .
Should not have
• Any kind of hamer, nails,screws, helmets itp. Please do not copy the other designs come up with something new.

```html
<!DOCTYPE html>
<html lang="en">
<head>
<meta charset="utf-8">
<title>Velmar Construction LLC – Business Card</title>
<link rel="stylesheet" href="https://fonts.googleapis.com/css2?family=Lato:wght@400;700;900&display=swap">
<style>
  :root {
    --navy: #0255a3;
    --white: #ffffff;
    --black: #000000;
    --orange: #f78f20;
    --grey-light: #b1b1b1;
    --grey: #9d9d9d;
    --ink: #1b1b1b;
    --sky: #33a6d7;
    --red: #ec1f27;
    --backdrop: #2e2e2e;
  }
  * { margin: 0; padding: 0; box-sizing: border-box; }
  html, body {
    width: 1200px; height: 900px; overflow: hidden;
    background: var(--backdrop);
    font-family: "Lato", Arial, sans-serif;
  }
  .canvas {
    position: relative; width: 1200px; height: 900px;
  }
  .card {
    position: absolute; left: 250px; width: 700px; height: 400px;
    border-radius: 28px; overflow: hidden;
    box-shadow: 0 12px 30px rgba(0,0,0,.45);
  }
  .card-front { top: 40px; }
  .card-back { top: 470px; background: var(--white); }

  .front-photo {
    position: absolute; inset: 0;
    background:
      radial-gradient(ellipse at 50% 10%, rgba(160,180,210,.35), transparent 55%),
      linear-gradient(170deg, #1a2a48 0%, #14213a 45%, #3a3f48 75%, #23262c 100%);
  }
  .front-name {
    position: absolute; left: 0; right: 0; top: 50%;
    transform: translateY(-50%);
    text-align: center;
    color: var(--white);
    font-weight: 900; font-size: 44px; letter-spacing: 3px;
  }

  .contact {
    position: absolute; left: 52px; top: 96px;
    color: var(--ink);
  }
  .holder-name {
    font-weight: 700; font-size: 22px; letter-spacing: 3px;
    text-transform: uppercase; margin-bottom: 14px;
  }
  .holder-first { color: var(--orange); }
  .holder-last { color: var(--navy); }
  .address { font-size: 19px; line-height: 1.25; margin-bottom: 14px; }
  .contact-list { list-style: none; font-size: 19px; line-height: 1.35; }
  .contact-list li { display: flex; align-items: center; gap: 12px; }
  .contact-list svg { width: 16px; height: 16px; flex: none; fill: var(--navy); }

  .brand {
    position: absolute; right: 48px; top: 150px;
    display: flex; align-items: center; gap: 12px;
  }
  .brand-mark { width: 22px; height: 22px; background: var(--orange); }
  .brand-name {
    font-weight: 900; font-size: 30px; letter-spacing: 1px;
    color: var(--black); line-height: 1.1; text-align: right;
  }
</style>
</head>
<body>
<main class="canvas">
  <section class="card card-front">
    <div class="front-photo" role="img" aria-label="Night photograph of high-rise buildings under construction with tower cranes"></div>
    <div class="front-name">VELMAR CONSTRUCTION LLC</div>
  </section>

  <section class="card card-back">
    <div class="contact">
      <p class="holder-name"><span class="holder-first">Gerald</span> <span class="holder-last">Tomasino</span></p>
      <p class="address">418 harbor 87th.<br>Dunmoor park ny 10352</p>
      <ul class="contact-list">
        <li>
          <svg viewBox="0 0 16 16"><path d="M3.6 1.2l2.3 2.6-1.3 1.8c.9 2 2.3 3.4 4.3 4.3l1.8-1.3 2.6 2.3-1.4 2.4C6.8 13.1 2.9 9.2 1.2 3.1z"/></svg>
          555-318-6094
        </li>
        <li>
          <svg viewBox="0 0 16 16"><path d="M4.5 1h7v14h-7zM6 2.5v9h4v-9zM7.3 12.6h1.4v1.2H7.3z" fill-rule="evenodd"/></svg>
          555-742-0583
        </li>
        <li>
          <svg viewBox="0 0 16 16"><path d="M1 3h14v10H1zm1.5 1.6v7h11v-7L8 8.6z M3 4.5l5 3.4 5-3.4z" fill-rule="evenodd"/></svg>
          velmarllc@tridomail.com
        </li>
        <li>
          <svg viewBox="0 0 16 16"><circle cx="8" cy="8" r="7"/><path d="M1 8h14M8 1c-2.5 2.5-2.5 11.5 0 14M8 1c2.5 2.5 2.5 11.5 0 14" stroke="#fff" stroke-width="1" fill="none"/></svg>
          www.velmarllc.com
        </li>
      </ul>
    </div>

    <div class="brand">
      <span class="brand-mark"></span>
      <span class="brand-name">VELMAR<br>CONSTRUCTION LLC</span>
    </div>
  </section>
</main>
</body>
</html>
```